Business Card Design Project

Build kick ass business card.
Updates

I just uploaded the Veruxo Logo in AI format, for those that were asking. It's looking real good and we'll be reviewing the designs soon. Thanks. 

Target Market(s)

Businesses in many verticals. Focusing on information security.

Veruxo, LLC
Darren Colby
Principal Security Consultant
Mobile: +1-480-555-0137
Email: Darren.Colby@Veruxo.example
Web: www.veruxo.example

Industry/Entity Type

Business

Requirements
Must have
• Design must look high-end, hi-tech stylish and minimalist

Be different – one that stands out from thousands of others

Does not have to be traditional rectangle

Would like logo integrated

```html
<!DOCTYPE html>
<html lang="en">
<head>
<meta charset="utf-8">
<title>Veruxo Business Card</title>
<link rel="stylesheet" href="https://fonts.googleapis.com/css2?family=Tinos&display=swap">
<style>
  :root {
    --backdrop: #121315;
    --card: #ffffff;
    --brand-blue: #0795d0;
    --ink: #333333;
    --title-light: #e2e6ea;
  }
  html, body {
    margin: 0;
    padding: 0;
    width: 809px;
    height: 1200px;
    overflow: hidden;
    background: var(--backdrop);
  }
  .canvas {
    position: relative;
    width: 809px;
    height: 1200px;
    font-family: "Tinos", "Times New Roman", serif;
  }
  .card {
    position: absolute;
    left: 127px;
    top: 128px;
    width: 547px;
    height: 957px;
    background: var(--card);
    overflow: hidden;
  }
  .band {
    position: absolute;
    left: 0;
    width: 100%;
    height: 25px;
    background: var(--brand-blue);
  }
  .band--top { top: 0; }
  .band--bottom { bottom: 0; }

  .brand {
    position: absolute;
    left: 60px;
    top: 210px;
    display: flex;
    align-items: center;
    gap: 26px;
  }
  .brand__mark {
    width: 92px;
    height: 92px;
    border-radius: 50%;
    background: var(--brand-blue);
  }
  .brand__name {
    font-size: 66px;
    letter-spacing: 4px;
    color: var(--ink);
    text-transform: uppercase;
    line-height: 1;
  }

  .nameplate {
    position: absolute;
    left: 68px;
    top: 422px;
    width: 430px;
    height: 86px;
    background: var(--brand-blue);
    box-shadow: 4px 5px 6px rgba(0, 0, 0, 0.55);
    text-transform: uppercase;
  }
  .nameplate__name {
    position: absolute;
    left: 40px;
    top: 16px;
    margin: 0;
    font-size: 27px;
    font-weight: 400;
    letter-spacing: 1.5px;
    word-spacing: 6px;
    color: var(--ink);
    line-height: 1;
  }
  .nameplate__title {
    position: absolute;
    left: 40px;
    top: 50px;
    margin: 0;
    font-size: 17.5px;
    letter-spacing: 0.8px;
    word-spacing: 4px;
    color: var(--title-light);
    line-height: 1;
  }

  .contact {
    position: absolute;
    left: 30px;
    top: 695px;
    width: 484px;
    height: 202px;
    border-radius: 50%;
    background: var(--brand-blue);
  }
  .contact__list {
    position: absolute;
    left: 92px;
    top: 58px;
    margin: 0;
    padding: 0;
    list-style: none;
    font-size: 17.5px;
    line-height: 23px;
    color: var(--ink);
    text-transform: uppercase;
  }
</style>
</head>
<body>
<div class="canvas">
  <section class="card" aria-label="Veruxo business card">
    <div class="band band--top"></div>

    <div class="brand">
      <div class="brand__mark"></div>
      <div class="brand__name">Veruxo</div>
    </div>

    <div class="nameplate">
      <h1 class="nameplate__name">Darren Colby</h1>
      <p class="nameplate__title">Principal Security Consultant</p>
    </div>

    <div class="contact">
      <ul class="contact__list">
        <li>Veruxo, LLC</li>
        <li>Mobile: +1-480-555-0137</li>
        <li>Email: Darren.Colby@Veruxo.example</li>
        <li>Web: www.veruxo.example</li>
      </ul>
    </div>

    <div class="band band--bottom"></div>
  </section>
</div>
</body>
</html>
```